Company Values - print for wall

We ned a print of our values on one of the walls in our office. Create a couple of suggestions that we can print on our walls.

Summary:
- See power point with values
- make two suggestion: one with only titles + one with titles and bulletpoints / use the "We" version)
- make a suggestion in a moon raiders theme
- see brand book for inspiration
- see images of office for inspiration
Updates

The company's values that we want to highlight are: 1. Exceed expectations 2. Execute with passion 3. Empower each other Exceed expectations:​ • We establish a good understanding of current expectations.​ • We provide helpful, honest, and timely feedback.​ • We deliver impressive quality.​ Execute with passion:​ • We embrace change.​ • We seek innovative solutions.​ • We inspire others with your actions and attitudes. ​ • We care about success. ​ • We are confident and humble. Empower each other:​ • We are available to help colleagues.​ • We are open-minded.​ • We seek and share information proactively.​ • We respect others’ time.​ This is in line with achieving the company vision: « Our vision is to make a difference for our customers through our highly customizable solutions for planning, execution, and analysis. It’s less about the software itself and more about customer success. Make better decisions faster with Clearmont. »​ Eirik Tove Malmberg, CEO Clearmont Company slogan: Better Decisions Faster​ It's a lot of text above, but what we what to emphasize most are the following text above and here again: exceed expectations, execute with passion, empower each other We can do something fun and cool with the Moon Raiders theme as this is internal - that's the visual that would work with the company culture.

Font styles to use
Sans Serif

Requirements
Nice to have
• - one suggestion with Montserrat font
- one suggestion in moon raiders font

```html
<!DOCTYPE html>
<html lang="en">
<head>
<meta charset="utf-8">
<title>Clearmont Values</title>
<link href="https://fonts.googleapis.com/css2?family=Montserrat:wght@500;700;800;900&display=swap" rel="stylesheet">
<style>
  :root {
    --paper: #ffffff;
    --slate: #474a4d;
    --slate-deep: #3f4245;
    --orange: #f2974b;
    --orange-soft: #e7a26a;
    --white: #ffffff;
  }
  html, body {
    margin: 0;
    padding: 0;
    width: 1200px;
    height: 1000px;
    overflow: hidden;
    background: var(--paper);
    font-family: "Montserrat", Arial, sans-serif;
  }
  .poster {
    position: absolute;
    left: 18px;
    top: 87px;
    width: 1162px;
    height: 820px;
    background: var(--slate);
    overflow: hidden;
    color: var(--white);
  }
  .scene-art {
    position: absolute;
    left: 0;
    top: 0;
    width: 900px;
    height: 720px;
  }
  .title-rule {
    position: absolute;
    left: 730px;
    top: 56px;
    width: 432px;
    height: 4px;
    background: var(--white);
  }
  .title-pill {
    position: absolute;
    left: 408px;
    top: 16px;
    width: 322px;
    height: 78px;
    border: 4px solid var(--white);
    border-radius: 44px;
    box-sizing: border-box;
    display: flex;
    align-items: center;
    justify-content: center;
  }
  .title-pill h1 {
    margin: 0;
    font-size: 66px;
    font-weight: 900;
    letter-spacing: -1px;
    line-height: 1;
    color: var(--white);
  }
  .values-panel {
    position: absolute;
    left: 410px;
    top: 108px;
    width: 752px;
    height: 540px;
    background: var(--slate);
    border-radius: 26px 0 0 26px;
    padding: 38px 0 0 28px;
    box-sizing: border-box;
  }
  .value-group { margin-bottom: 23px; }
  .value-group h2 {
    margin: 0 0 4px;
    font-size: 17px;
    font-weight: 800;
    letter-spacing: 0.2px;
  }
  .value-group ul {
    list-style: none;
    margin: 0;
    padding: 0;
  }
  .value-group li {
    position: relative;
    padding-left: 24px;
    font-size: 19px;
    font-weight: 700;
    line-height: 29px;
    letter-spacing: 0.2px;
  }
  .value-group li::before {
    content: "";
    position: absolute;
    left: 2px;
    top: 9px;
    width: 12px;
    height: 12px;
    border-radius: 50%;
    background: var(--white);
  }
  .vision {
    position: absolute;
    left: 32px;
    top: 698px;
    width: 800px;
  }
  .vision blockquote {
    margin: 0;
    font-size: 15.5px;
    font-weight: 700;
    line-height: 22px;
  }
  .vision .attribution {
    margin: 12px 0 0;
    font-size: 14px;
    font-weight: 500;
  }
  .vision .attribution strong { font-weight: 800; }
  .brand {
    position: absolute;
    left: 880px;
    top: 718px;
    width: 270px;
    text-align: center;
  }
  .brand .wordmark {
    margin: 0;
    font-size: 30px;
    font-weight: 800;
    letter-spacing: -0.5px;
  }
  .brand .slogan {
    margin: 14px 0 0;
    font-size: 19px;
    font-weight: 700;
  }
</style>
</head>
<body>
  <main class="poster">
    <svg class="scene-art" role="img" aria-label="Moon Raiders themed halftone illustration of a giant walker with a lone figure standing on a hill" viewBox="0 0 900 720">
      <defs>
        <linearGradient id="sceneFade" x1="0" y1="0" x2="1" y2="0">
          <stop offset="0" stop-color="#f2974b"/>
          <stop offset="0.5" stop-color="#eb9a58"/>
          <stop offset="0.8" stop-color="#b9825a"/>
          <stop offset="1" stop-color="#474a4d"/>
        </linearGradient>
        <linearGradient id="sceneFloor" x1="0" y1="0" x2="0" y2="1">
          <stop offset="0.75" stop-color="#474a4d" stop-opacity="0"/>
          <stop offset="1" stop-color="#474a4d"/>
        </linearGradient>
      </defs>
      <rect width="900" height="720" fill="url(#sceneFade)"/>
      <rect width="900" height="720" fill="url(#sceneFloor)"/>
    </svg>

    <div class="title-rule"></div>
    <div class="title-pill"><h1>VALUES</h1></div>

    <section class="values-panel">
      <div class="value-group">
        <h2>EXCEED EXPECTATIONS:</h2>
        <ul>
          <li>We establish a good understanding of current expectations.</li>
          <li>We provide helpful, honest, and timely feedback.</li>
          <li>We deliver impressive quality.</li>
        </ul>
      </div>
      <div class="value-group">
        <h2>EXECUTE WITH PASSION:</h2>
        <ul>
          <li>We embrace change.</li>
          <li>We seek innovative solutions.</li>
          <li>We inspire others with your actions and attitudes.</li>
          <li>We care about success.</li>
          <li>We are confident and humble.</li>
        </ul>
      </div>
      <div class="value-group">
        <h2>EMPOWER EACH OTHER:</h2>
        <ul>
          <li>We are available to help colleagues.</li>
          <li>We are open-minded.</li>
          <li>We seek and share information proactively.</li>
          <li>We respect others’ time.</li>
        </ul>
      </div>
    </section>

    <footer class="vision">
      <blockquote>“Our vision is to make a difference for our customers through our highly customizable solutions for planning, execution, and analysis. It’s less about the software itself and more about customer success. Make better decisions faster with Clearmont.”</blockquote>
      <p class="attribution"><strong>Eirik Tove Malmberg</strong>, CEO Clearmont Company</p>
    </footer>

    <div class="brand">
      <p class="wordmark">Clearmont</p>
      <p class="slogan">Better Decisions Faster</p>
    </div>
  </main>
</body>
</html>
```